Local business providing residential house cleaning services

We need a business card design that is "cute" or "cartoonish" while still maintaining a professional appeal. Tidy Nook Cleaners is the name. We would like to use a "pin up girl" or maid next to the name with a broom or vacuum cleaner. We want the look to have a 50's American look to it. We are not sure if we want the pin up girl in a maid outfit or with a broom or vacuum cleaner but we hope some of you will be able to take these ideas and be creative. If you have any questions at all please don't hesitate to message me so that we can get the best design possible. Thank you very much and I look forward to seeing some designs! Mira Delgado

Target Market(s)

Upper class Americans that are busy and have money and want to come home to a clean house.

Industry/Entity Type

Cleaning Service

Contact Information for Business Card

Pin up girl incorporated into the card is a must.

Font styles to use
Decorative
Script

Requirements
Must have
• Pin up girl
Nice to have
• A crown used on the Q possibly.

```html
<!DOCTYPE html>
<html lang="en">
<head>
<meta charset="utf-8">
<title>Tidy Nook Cleaners – Business Card</title>
<link href="https://fonts.googleapis.com/css2?family=Open+Sans:wght@400;600;700&display=swap" rel="stylesheet">
<style>
  :root {
    --backdrop: #ecebe8;
    --card-white: #ffffff;
    --brand-purple: #9e479c;
    --brand-magenta: #c51ad6;
    --brand-brown: #4a2a1c;
    --text-grey: #3d3a38;
    --card-shadow: 0 6px 18px rgba(0,0,0,0.18);
  }
  * { margin: 0; padding: 0; box-sizing: border-box; }
  html, body { width: 1200px; height: 900px; overflow: hidden; }
  body {
    background: var(--backdrop);
    font-family: "Open Sans", Arial, sans-serif;
    position: relative;
  }
  .card {
    position: absolute;
    width: 620px;
    height: 354px;
    box-shadow: var(--card-shadow);
    overflow: hidden;
  }
  /* Back of card */
  .card-back {
    left: 500px;
    top: 70px;
    background: var(--brand-purple);
  }
  .card-back .brand {
    position: absolute;
    left: 150px;
    top: 128px;
    display: flex;
    align-items: center;
    gap: 16px;
  }
  .brand-square {
    width: 22px;
    height: 22px;
    flex: none;
  }
  .card-back .brand-square { background: var(--card-white); }
  .card-back .brand-name {
    color: var(--card-white);
    font-size: 40px;
    font-weight: 400;
    line-height: 1.1;
  }
  /* Front of card */
  .card-front {
    left: 80px;
    top: 476px;
    background: var(--card-white);
  }
  .card-front .decor {
    position: absolute;
    inset: 0;
  }
  .holder {
    position: absolute;
    left: 86px;
    top: 22px;
  }
  .holder-name {
    color: var(--brand-magenta);
    font-weight: 700;
    font-size: 19px;
    line-height: 1.1;
  }
  .holder-title {
    color: var(--text-grey);
    font-size: 13px;
    margin-top: 1px;
  }
  .contact {
    position: absolute;
    left: 40px;
    top: 138px;
    color: var(--text-grey);
    font-size: 14px;
    line-height: 19px;
    list-style: none;
  }
  .contact li { display: flex; align-items: center; gap: 8px; }
  .contact .address { padding-left: 18px; }
  .contact svg { width: 10px; height: 10px; flex: none; fill: var(--brand-magenta); }
  .card-front .brand {
    position: absolute;
    left: 360px;
    top: 132px;
    display: flex;
    align-items: center;
    gap: 12px;
  }
  .card-front .brand-square { background: var(--brand-brown); }
  .card-front .brand-name {
    color: var(--brand-magenta);
    font-size: 32px;
    font-weight: 400;
    line-height: 1.1;
  }
</style>
</head>
<body>

  <section class="card card-back" aria-label="Card back">
    <div class="brand">
      <span class="brand-square"></span>
      <span class="brand-name">Tidy Nook<br>Cleaners</span>
    </div>
  </section>

  <section class="card card-front" aria-label="Card front">
    <svg class="decor" viewBox="0 0 620 354" aria-hidden="true">
      <polygon points="0,0 58,0 0,34" fill="var(--brand-magenta)"/>
      <polygon points="64,0 82,0 60,32 22,32" fill="var(--brand-brown)"/>
      <polygon points="0,262 286,262 306,292 0,292" fill="var(--brand-magenta)"/>
      <polygon points="312,296 620,296 620,354 350,354" fill="var(--brand-brown)"/>
    </svg>

    <div class="holder">
      <p class="holder-name">Owen Hartley</p>
      <p class="holder-title">Managing Director</p>
    </div>

    <ul class="contact">
      <li class="address">12345, Address Goes Here</li>
      <li class="address">Country Name, 123456.</li>
      <li><svg viewBox="0 0 10 10"><path d="M2 0h2l1 3-1.5 1a6 6 0 0 0 2.5 2.5L7 5l3 1v2a2 2 0 0 1-2 2A8 8 0 0 1 0 2a2 2 0 0 1 2-2z"/></svg>044-555 018 274</li>
      <li><svg viewBox="0 0 10 10"><path d="M0 2h10v6H0z M0 2l5 3 5-3" stroke="#fff" stroke-width="0.8"/></svg>info@tidynook.com</li>
      <li><svg viewBox="0 0 10 10"><circle cx="5" cy="5" r="5"/></svg>www.tidynookcleaners.com</li>
    </ul>

    <div class="brand">
      <span class="brand-square"></span>
      <span class="brand-name">Tidy Nook<br>Cleaners</span>
    </div>
  </section>

</body>
</html>
```